Get me out of Jail business cards!!!!

I need business cards done for my business. I own a BailBonds and I get people out of jail!

Colors are red white and black

I need it to say on the card these details:

Rollin’ Free Bailbonds

452 S Kettering Ave
Arcadia, FL 34266

863-555-0172

Open 24/7

On the back of the card:

Must check in every Tuesday.

______/______/______ court date
____________________ time
You must know your court date at all times!

Marla Tisdell - owner
Rosalind Tisdell - agent
Denise Crandon - agent

Industry/Entity Type

Bail bonds

Contact Information for Business Card

Colors are red white and black I need it to say on the card these details: Rollin’ Free Bailbonds 452 S Kettering Ave Arcadia, FL 34266 863-555-0172 Open 24/7 On the back of the card: Must check in every Tuesday. ______/______/______ court date ____________________ time You must know your court date at all times! Marla Tisdell - owner Rosalind Tisdell - agent Denise Crandon - agent

Font styles to use
Serif
Sans Serif

Colors
EB3D1F
EC4F4E
F09395
F8D3D4
FCEDEE

Requirements
Must have
• I listed the must haves in the business card details
Nice to have
• Handcuffs or jail bars or a man in a black and white suit

```html
<!DOCTYPE html>
<html lang="en">
<head>
<meta charset="utf-8">
<title>Rollin’ Free Bailbonds – Business Card</title>
<link rel="stylesheet" href="https://fonts.googleapis.com/css2?family=Montserrat:wght@400;500;600&family=Roboto+Condensed:wght@700&family=Zilla+Slab:wght@700&family=Oswald:wght@600&display=swap">
<style>
  :root {
    --stage: #999999;
    --paper: #ffffff;
    --ink: #111111;
    --red: #eb1c1c;
    --red-dark: #9e0f0f;
    --grey: #7a7a7a;
    --night: #0b0b0b;
    --night-soft: #2a2a2a;
  }
  * { margin: 0; padding: 0; box-sizing: border-box; }
  html, body { width: 1200px; height: 1200px; overflow: hidden; background: var(--stage); }
  .canvas { position: relative; width: 1200px; height: 1200px; }

  .card { position: absolute; left: 201px; width: 798px; height: 466px; overflow: hidden; }
  .card--back { top: 84px; background: var(--paper); color: var(--ink); }
  .card--front { top: 600px; background: var(--night); color: var(--paper); }

  .centered { position: absolute; transform: translateX(-50%); text-align: center; white-space: nowrap; }

  /* back side */
  .brand-name {
    left: 210px; top: 140px;
    font-family: "Montserrat", sans-serif; font-weight: 500; color: var(--ink); line-height: 1;
  }
  .brand-name span { display: block; }
  .brand-name .line-1 { font-size: 30px; }
  .brand-name .line-2 { font-size: 48px; margin-top: 4px; }
  .staff { left: 210px; top: 250px; font: 700 19px/27px "Roboto Condensed", sans-serif; }
  .staff__name { color: var(--red); }
  .staff__role { color: var(--ink); }

  .checkin {
    left: 573px; top: 140px;
    font: 700 23px/1 "Zilla Slab", serif; color: var(--red); letter-spacing: -0.3px;
  }
  .fill-line { position: absolute; height: 2px; background: var(--grey); }
  .fill-line--date { left: 443px; width: 260px; top: 209px; }
  .date-slash { position: absolute; top: 186px; font: 400 22px/1 "Montserrat", sans-serif; color: var(--grey); }
  .fill-line--time { left: 438px; width: 270px; top: 278px; }
  .field-label { left: 573px; font: 400 20px/1 "Montserrat", sans-serif; color: var(--grey); }
  .field-label--date { top: 218px; }
  .field-colon { left: 573px; top: 250px; font: 400 18px/1 "Montserrat", sans-serif; color: var(--grey); }
  .field-label--time { top: 292px; }
  .reminder { left: 573px; top: 338px; font: 600 17px/22px "Montserrat", sans-serif; color: var(--ink); }

  /* front side */
  .bars-backdrop {
    position: absolute; inset: 0;
    background: radial-gradient(ellipse at 50% 45%, var(--night-soft) 0%, var(--night) 75%);
  }
  .front-name { left: 399px; top: 110px; font-family: "Montserrat", sans-serif; font-weight: 500; line-height: 1; color: var(--paper); }
  .front-name span { display: block; }
  .front-name .line-1 { font-size: 72px; }
  .front-name .line-2 { font-size: 96px; margin-top: 2px; }

  .hours-band {
    position: absolute; left: 150px; top: 312px; width: 511px; height: 34px;
    background: linear-gradient(90deg, var(--red-dark) 0%, var(--red) 30%, var(--red) 70%, var(--red-dark) 100%);
  }
  .hours-band__text {
    position: absolute; left: 50%; top: 50%; transform: translate(-50%, -50%);
    font: 700 28px/1 "Zilla Slab", serif; color: var(--night); letter-spacing: 1px; white-space: nowrap;
  }
  .phone { position: absolute; left: 153px; top: 372px; display: flex; align-items: center; gap: 10px; }
  .phone svg { width: 32px; height: 32px; }
  .phone__number { font: 600 36px/1 "Oswald", sans-serif; color: var(--paper); letter-spacing: 0.5px; }
  .address { position: absolute; left: 473px; top: 362px; font: 500 21px/28px "Montserrat", sans-serif; font-style: normal; color: var(--paper); }
</style>
</head>
<body>
<main class="canvas">

  <section class="card card--back" aria-label="Card back">
    <div class="centered brand-name"><span class="line-1">Rollin’ Free</span><span class="line-2">Bailbonds</span></div>
    <div class="centered staff">
      <div><span class="staff__name">Marla Tisdell</span> <span class="staff__role">• owner</span></div>
      <div><span class="staff__name">Rosalind Tisdell</span> <span class="staff__role">• agent</span></div>
      <div><span class="staff__name">Denise Crandon</span> <span class="staff__role">• agent</span></div>
    </div>

    <div class="centered checkin">Must check in every Tuesday.</div>
    <div class="fill-line fill-line--date"></div>
    <span class="date-slash" style="left:529px">/</span>
    <span class="date-slash" style="left:609px">/</span>
    <div class="centered field-label field-label--date">court date</div>
    <div class="centered field-colon">:</div>
    <div class="fill-line fill-line--time"></div>
    <div class="centered field-label field-label--time">time</div>
    <div class="centered reminder">You must know your court<br>date at all times!</div>
  </section>

  <section class="card card--front" aria-label="Card front">
    <div class="bars-backdrop" role="img" aria-label="Dark backdrop of jail cell bars"></div>
    <div class="centered front-name"><span class="line-1">Rollin’ Free</span><span class="line-2">Bailbonds</span></div>
    <div class="hours-band"><span class="hours-band__text">OPEN 24/7</span></div>
    <div class="phone">
      <svg viewBox="0 0 32 32" aria-hidden="true">
        <circle cx="16" cy="16" r="16" fill="var(--red)"/>
        <path d="M11.2 8.5c.6-.3 1.3-.1 1.6.5l1.5 3c.3.6.1 1.2-.4 1.6l-1.2.9c.9 2 2.5 3.7 4.6 4.7l.9-1.2c.4-.5 1.1-.7 1.6-.4l3 1.5c.6.3.8 1 .5 1.6l-.9 1.9c-.4.8-1.3 1.2-2.2 1-6-1.4-10.5-6-11.9-11.9-.2-.9.2-1.8 1-2.2z" fill="var(--night)"/>
      </svg>
      <span class="phone__number">863•555•0172</span>
    </div>
    <address class="address">452 S Kettering Ave<br>Arcadia, FL 34266</address>
  </section>

</main>
</body>
</html>
```